Building Referrer Relationships Booklet

4 page A4 booklet to give to potential professional referrers to establish a collaborative relationship.Needs to be bright, vibrant, colourful, friendly, inviting, in keeping with The Wren Clinic colours.
Want to provide potential referrer partners a great reason to choose to collaborate with us. They need to know who we are, what makes us different/appealing, and who we are looking for to connect with.
The final product should communicate high performance and connectedness.

Target Market(s)

professional medical allied health and fitness practitioners

Industry/Entity Type

Health

Requirements
Must have
• energetic, vibrant, engaging, inviting, images

```html
<!DOCTYPE html>
<html lang="en">
<head>
<meta charset="utf-8">
<title>The Wren Clinic – About Us &amp; Our Team</title>
<link rel="stylesheet" href="https://fonts.googleapis.com/css2?family=Arimo:ital,wght@0,400;0,700;1,700&display=swap">
<style>
:root{
  --orange:#e0470f;
  --blue:#1f9bc8;
  --ink:#141414;
  --left-bg-a:#d7eef7;
  --left-bg-b:#f6fbfd;
  --white:#ffffff;
}
*{box-sizing:border-box;margin:0;padding:0}
html,body{width:1200px;height:903px;overflow:hidden;background:var(--white)}
body{font-family:"Arimo",Arial,sans-serif;color:var(--ink)}
.spread{position:relative;width:1200px;height:903px;overflow:hidden}
.page-left{position:absolute;left:0;top:0;width:585px;height:903px;
  background:linear-gradient(90deg,var(--left-bg-a) 0%,var(--left-bg-b) 100%)}
.page-right{position:absolute;left:588px;top:0;width:612px;height:903px;
  background:linear-gradient(180deg,#eeeeee 0%,#e6e6e6 100%)}
.section-title{position:absolute;color:var(--orange);font-weight:700;font-size:19px;letter-spacing:.2px}
.values{position:absolute;left:45px;top:80px;width:480px;font-size:15px;line-height:20px}
.values p{margin-bottom:19px}
.values b{font-weight:700}
.line{display:block;white-space:nowrap;text-align:justify;text-align-last:justify}
.line.end{text-align-last:left}
.tagline{position:absolute;left:45px;top:459px;width:490px;text-align:center;color:var(--blue);
  font-weight:700;font-style:italic;font-size:16.5px;line-height:21.5px}
.love-title{position:absolute;left:45px;top:543px;color:var(--orange);font-weight:700;font-size:17px;line-height:22px}
.love-list{position:absolute;left:52px;top:610px;width:474px;list-style:none;font-size:15px;line-height:20px}
.love-list li{position:absolute;left:0;width:474px}
.love-list .mark{position:absolute;left:0;width:22px;height:22px;background:var(--orange)}
.love-list .text{position:absolute;left:51px;width:423px}
.member{position:absolute;width:240px;text-align:center}
.photo{display:flex;margin:0 auto;width:116px;height:116px;border-radius:13px;
  background:linear-gradient(180deg,#f7f7f7,#e9e9e9);border:1px solid #9c9c9c;
  align-items:center;padding-left:4px;text-align:left;
  color:var(--orange);font-weight:700;font-size:16px;line-height:17px}
.name{margin-top:13px;font-weight:700;font-size:15px;letter-spacing:.1px}
.role{margin:4px auto 0;width:186px;height:28px;background:var(--orange);color:var(--white);
  font-weight:700;font-size:15px;line-height:28px;box-shadow:2px 3px 3px rgba(0,0,0,.25)}
.credentials{position:absolute;left:736px;top:700px;width:352px;height:178px;border-radius:20px;
  background:var(--orange);color:var(--white);font-size:14px;line-height:18.8px;padding:14px 0 0 14px;
  box-shadow:0 3px 6px rgba(0,0,0,.2)}
.credentials li{list-style:none;white-space:nowrap}
.star::before{content:"★"}
</style>
</head>
<body>
<div class="spread">
  <section class="page-left" role="img" aria-label="Background of faint medical icons on pale blue"></section>
  <section class="page-right" role="img" aria-label="Background of faint grey medical and hospital icons"></section>

  <h2 class="section-title" style="left:45px;top:33px">ABOUT US</h2>
  <div class="values">
    <p><span class="line end"><b>Courage</b> gives us the strength and confidence to take risks and</span><span class="line end">embrace challenges</span></p>
    <p><span class="line"><b>Inspiration</b> is our energy, our fuel for success, that life force that</span><span class="line end">feeds us as we grow and develop.</span></p>
    <p><span class="line"><b>Fun</b> generates happiness, and we all function at our best when</span><span class="line end">we are happy.</span></p>
    <p><span class="line end"><b>Creativity</b> sets us as an innovative leading-edge business.</span></p>
    <p><span class="line"><b>Wow</b> means being the very best we can be and realise our true</span><span class="line">potential. We are not your average business, our service is not</span><span class="line end">average, and our people are not average.</span></p>
    <p><span class="line"><b>Team</b> and in particular high-performance team means we perform</span><span class="line">at our very best. Great teamwork creates unity and we accomplish</span><span class="line end">much more than each of us alone.</span></p>
  </div>
  <p class="tagline">AT THE WREN CLINIC, WE ARE PASSIONATE<br>ABOUT BUILDING STRONG POSTURAL FOUNDATIONS,<br>FROM THE FEET UP.</p>
  <h3 class="love-title">THE TOP 3 THINGS OUR CLIENTS LOVE ABOUT US<br>(AND HOPEFULLY YOURS WILL TOO!):</h3>
  <ul class="love-list">
    <li style="top:0"><span class="mark" style="top:10px"></span><span class="text"><span class="line end">Positive energy, enthusiasm and outcomes</span><span class="line end">NPS average score &gt;9 out of 10</span></span></li>
    <li style="top:60px"><span class="mark" style="top:18px"></span><span class="text"><span class="line end">Trusted leader in the practice of podiatric medicine</span><span class="line">established 1999, elite experience, latest high-tech</span><span class="line end">equipment</span></span></li>
    <li style="top:140px"><span class="mark" style="top:0"></span><span class="text"><span class="line end">Focus is on strong feet, not just orthotics! WBFA Barefoot</span><span class="line end">Technology, Fascial Lines, Foot Manual Therapies</span></span></li>
  </ul>

  <h2 class="section-title" style="left:614px;top:33px">OUR TEAM:</h2>

  <div class="member" style="left:669px;top:77px">
    <div class="photo" role="img" aria-label="Portrait photo of Dr. Marcus Delacroix">DR PiC<br>SHOULD GO<br>HERE</div>
    <div class="name">DR. MARCUS DELACROIX</div>
    <div class="role">Principal Podiatrist</div>
  </div>
  <div class="member" style="left:914px;top:77px">
    <div class="photo" role="img" aria-label="Portrait photo of Dr. Elena Whitford">DR PiC<br>SHOULD GO<br>HERE</div>
    <div class="name">DR. ELENA WHITFORD</div>
    <div class="role">Senior Podiatrist</div>
  </div>
  <div class="member" style="left:671px;top:277px">
    <div class="photo" role="img" aria-label="Portrait photo of Dr. Tobias Lin">DR PiC<br>SHOULD GO<br>HERE</div>
    <div class="name" style="margin-top:10px">DR. TOBIAS LIN</div>
    <div class="role">Podiatrist</div>
  </div>
  <div class="member" style="left:917px;top:277px">
    <div class="photo" role="img" aria-label="Portrait photo of Dr. Rosalind Carver">DR PiC<br>SHOULD GO<br>HERE</div>
    <div class="name" style="margin-top:10px">DR. ROSALIND CARVER</div>
    <div class="role">Podiatrist</div>
  </div>
  <div class="member" style="left:671px;top:477px">
    <div class="photo" role="img" aria-label="Portrait photo of Mira Halden">DR PiC<br>SHOULD GO<br>HERE</div>
    <div class="name" style="margin-top:12px">MIRA HALDEN</div>
    <div class="role">Practice Manager</div>
  </div>
  <div class="member" style="left:917px;top:477px">
    <div class="photo" role="img" aria-label="Portrait photo of Jodie Parrish">DR PiC<br>SHOULD GO<br>HERE</div>
    <div class="name" style="margin-top:12px">JODIE PARRISH</div>
    <div class="role">Front Office Admin</div>
  </div>

  <ul class="credentials">
    <li class="star">Director, Sports Health Collective (SHC)</li>
    <li class="star">Director, Pacific College of Podiatric</li>
    <li>Sports Care (PCPSC).</li>
    <li class="star">External Advisor, Westbay University Podiatric Unit</li>
    <li class="star">WBFA Level 1 Barefoot Rehabilitation Instructor</li>
    <li class="star">Foot Manual Therapies trained</li>
    <li class="star">Fascial Lines trained</li>
    <li class="star">Class 3b Laser Certified</li>
  </ul>
</div>
</body>
</html>
```